Caldwen Primary School

We need to improve on our designs for a local School, Caldwen Primary.
One file contains the correct information required on the sign.
Our Mock ups are suggestions.
The School Uniform is blue -
We had these comments from our Client.
I can't decide whether to change the blue and try green to represent our commitment to outdoors, or maybe a combination of colours from the school badge, For the main sign options , I like them both but wondered if there was a way of combining the two? Slightly bigger badge.

I've included the files for the smaller signs if you were happy to provide a service to include all. We are a sign business focusing on other projects and external support will help. Thanks - Oscar.

```html
<!DOCTYPE html>
<html lang="en">
<head>
<meta charset="utf-8">
<title>Caldwen Primary School – Entrance Sign</title>
<link rel="stylesheet" href="https://fonts.googleapis.com/css2?family=Barlow+Condensed:wght@700&family=Poppins:wght@600&display=swap">
<style>
  :root {
    --backdrop: #b1b1b1;
    --school-blue: #2571b9;
    --sign-white: #ffffff;
    --sun-orange: #f29a16;
    --meadow-green: #4caf3f;
    --leaf-lime: #a6c92a;
  }
  html, body {
    margin: 0;
    padding: 0;
    width: 1200px;
    height: 874px;
    overflow: hidden;
    background: var(--backdrop);
  }
  .sign {
    display: block;
    width: 1200px;
    height: 874px;
  }
  .sign__frame { fill: var(--school-blue); }
  .sign__panel { fill: var(--sign-white); }
  .sign__band { fill: var(--school-blue); }
  .motto {
    font-family: "Poppins", sans-serif;
    font-weight: 600;
    font-size: 34px;
    fill: var(--sign-white);
    text-anchor: middle;
  }
  .badge__disc { fill: var(--sun-orange); stroke: var(--sign-white); stroke-width: 4; }
  .badge__name {
    font-family: "Poppins", sans-serif;
    font-weight: 600;
    font-size: 24px;
    fill: var(--sign-white);
    text-anchor: middle;
  }
  .school-name {
    font-family: "Barlow Condensed", sans-serif;
    font-weight: 700;
    font-size: 74px;
    letter-spacing: 1px;
  }
  .school-name--english { fill: var(--sun-orange); }
  .school-name--welsh { fill: var(--meadow-green); }
  .contact {
    font-family: "Poppins", sans-serif;
    font-weight: 600;
    fill: var(--school-blue);
  }
  .contact--head { font-size: 25px; text-anchor: middle; }
  .contact--phone { font-size: 26px; }
  .phone-icon__disc { fill: var(--leaf-lime); }
  .phone-icon__handset { fill: var(--sign-white); }
  .council__name {
    font-family: "Barlow Condensed", sans-serif;
    font-weight: 700;
    font-size: 15px;
    fill: var(--school-blue);
  }
  .council__square { fill: var(--school-blue); }
</style>
</head>
<body>
<svg class="sign" viewBox="0 0 1200 874" xmlns="http://www.w3.org/2000/svg">
  <path class="sign__frame" d="M210,305 Q210,275 240,275 L310,275 Q325,275 336,264 C400,205 500,186 600,186 C700,186 800,205 864,264 Q875,275 890,275 L960,275 Q990,275 990,305 L990,660 Q990,687 963,687 L237,687 Q210,687 210,660 Z"/>
  <path class="sign__panel" d="M223,307 Q223,288 242,288 L310,288 Q330,288 345,274 C405,218 500,199 600,199 C700,199 795,218 855,274 Q870,288 890,288 L958,288 Q977,288 977,307 L977,660 Q977,675 962,675 L238,675 Q223,675 223,660 Z"/>
  <path class="sign__band" d="M229,310 Q229,294 245,294 L310,294 Q333,294 350,279 C410,224 500,205 600,205 C700,205 790,224 850,279 Q867,294 890,294 L955,294 Q971,294 971,310 L971,412 L229,412 Z"/>

  <text class="motto" x="372" y="351">Wings to fly</text>
  <text class="motto" x="832" y="351">Roots to Grow</text>

  <g class="badge">
    <circle class="badge__disc" cx="600" cy="308" r="93"/>
    <text class="badge__name" x="600" y="302">Caldwen</text>
    <text class="badge__name" x="600" y="332">Primary</text>
  </g>

  <text class="school-name school-name--english" x="258" y="489" textLength="684" lengthAdjust="spacingAndGlyphs">CALDWEN PRIMARY SCHOOL</text>
  <text class="school-name school-name--welsh" x="258" y="559" textLength="686" lengthAdjust="spacingAndGlyphs">YSGOL GYNRADD CALDWEN</text>

  <text class="contact contact--head" x="600" y="607">Headteacher/Pennaeth - Mr T. Ellery</text>
  <g class="phone-icon">
    <circle class="phone-icon__disc" cx="515" cy="631" r="14"/>
    <path class="phone-icon__handset" d="M509,622 q2,-1 4,1 l2,3 q1,2 -1,3 l-1,1 q1,3 4,6 l1,-1 q1,-2 3,-1 l3,2 q2,2 1,4 l-1,1 q-3,3 -8,0 q-6,-4 -9,-10 q-2,-5 1,-8 z"/>
  </g>
  <text class="contact contact--phone" x="539" y="641">01632 960418</text>

  <g class="council">
    <rect class="council__square" x="858" y="598" width="26" height="26"/>
    <text class="council__name" x="890" y="609">TARREN</text>
    <text class="council__name" x="890" y="625">COUNCIL</text>
  </g>
</svg>
</body>
</html>
```